Business card for STEADYWAVE

Please design professional business card for IT consulting firm STEADYWAVE INC.
Use logo attached.
Use information from sample qNode business card attached.
replace qnode inc with STEADYWAVE INC.
as well as qnodeinc.com with steadywave.example

```html
<!DOCTYPE html>
<html lang="en">
<head>
<meta charset="utf-8">
<title>STEADYWAVE business card</title>
<link href="https://fonts.googleapis.com/css2?family=Montserrat:wght@600;800&family=Roboto:wght@400;500;700&family=Roboto+Condensed:wght@700&display=swap" rel="stylesheet">
<style>
  :root{
    --stage:#2f3234;
    --paper:#ffffff;
    --ink:#141414;
    --text:#2a2a2a;
    --violet:#8a1fe0;
    --card-dark:#1d1d1e;
    --silver:#d8d8d8;
    --edge:linear-gradient(var(--dir,180deg),#8a1fe0 0%,#b01fc8 22%,#f0567a 42%,#f7941d 55%,#45c9f5 80%,#3ef0c8 100%);
  }
  *{box-sizing:border-box;margin:0;padding:0}
  html,body{width:1200px;height:800px;overflow:hidden;background:var(--stage)}
  .stage{width:1200px;height:800px;display:flex;align-items:center;justify-content:center;gap:40px}
  .card{position:relative;width:540px;height:309px;border-radius:18px;overflow:hidden;box-shadow:0 14px 34px rgba(0,0,0,.45)}

  /* front */
  .card--front{background:var(--paper);font-family:"Roboto",sans-serif;color:var(--text)}
  .edge-strip--left{position:absolute;left:0;top:0;bottom:0;width:8px;background:var(--edge)}
  .front-logo{position:absolute;left:38px;top:44px;display:flex;align-items:center;gap:8px}
  .wordmark{font-family:"Montserrat",sans-serif;font-weight:800;font-size:27px;letter-spacing:3px;color:var(--ink)}
  .logo-square{width:11px;height:11px;background:var(--violet)}
  .name-panel{position:absolute;right:0;top:56px;width:260px;height:116px;
    background:linear-gradient(120deg,#f1e3fb 0%,#eaf0fc 50%,#e4faf4 100%)}
  .name-block{position:absolute;left:28px;top:26px}
  .person-name{font-family:"Roboto Condensed",sans-serif;font-weight:700;font-size:21px;color:var(--ink);letter-spacing:.3px}
  .credential{font-family:"Roboto Condensed",sans-serif;font-weight:700;font-size:10px;color:var(--ink);text-align:right;margin-top:2px}
  .job-title{font-size:14px;color:var(--violet);letter-spacing:.8px;margin-top:4px}
  .contact-list{position:absolute;left:38px;top:122px;list-style:none;font-size:11.5px;line-height:15px}
  .contact-list li{display:flex;align-items:flex-start;gap:9px}
  .contact-list .icon{width:11px;height:11px;margin-top:2px;flex:none;fill:var(--violet)}
  .contact-list .company{font-weight:700;color:var(--ink)}
  .contact-list .group{margin-top:6px}

  /* back */
  .card--back{background:var(--card-dark)}
  .edge-strip--bottom{position:absolute;left:0;right:0;bottom:0;height:8px;--dir:270deg;background:var(--edge)}
  .back-logo{position:absolute;inset:0 0 8px 0;display:flex;align-items:center;justify-content:center;gap:12px}
  .back-logo .wordmark{font-weight:600;font-size:44px;letter-spacing:5px;color:var(--silver)}
  .back-logo .logo-square{width:18px;height:18px}
</style>
</head>
<body>
<main class="stage">
  <section class="card card--front" aria-label="Card front">
    <div class="edge-strip--left"></div>
    <div class="front-logo">
      <span class="wordmark">STEADYWAVE</span>
      <span class="logo-square"></span>
    </div>
    <div class="name-panel">
      <div class="name-block">
        <p class="person-name">DORIAN VELASKO</p>
        <p class="credential">P.ENG.</p>
        <p class="job-title">General Manager</p>
      </div>
    </div>
    <ul class="contact-list">
      <li>
        <svg class="icon" viewBox="0 0 12 12"><path d="M6 0a4 4 0 0 0-4 4c0 3 4 8 4 8s4-5 4-8a4 4 0 0 0-4-4zm0 5.6A1.6 1.6 0 1 1 6 2.4a1.6 1.6 0 0 1 0 3.2z"/></svg>
        <div><span class="company">STEADYWAVE INC.</span><br>1280 Larkfield Rd., Suite 101<br>Westbrook, Ontario,<br>K0A 2B4, Canada</div>
      </li>
      <li class="group">
        <svg class="icon" viewBox="0 0 12 12"><path d="M2.4 0.6l2 2-1 1.4c.7 1.6 2 2.9 3.6 3.6l1.4-1 2 2-1.3 1.9C4.6 10.2 1.8 7.4.5 2z"/></svg>
        <div>(555) 214-0370 ext.201</div>
      </li>
      <li>
        <svg class="icon" viewBox="0 0 12 12"><path d="M3 0h6a1 1 0 0 1 1 1v10a1 1 0 0 1-1 1H3a1 1 0 0 1-1-1V1a1 1 0 0 1 1-1zm.5 1.5v8h5v-8zM6 10.2a.6.6 0 1 0 0 1.2.6.6 0 0 0 0-1.2z"/></svg>
        <div>(555) 387-1069</div>
      </li>
      <li>
        <svg class="icon" viewBox="0 0 12 12"><path d="M0 2h12v8H0zm1 1v.4l5 3.2 5-3.2V3zm0 1.6V9h10V4.6L6 7.8z"/></svg>
        <div>dvelasko@steadywave.example</div>
      </li>
      <li>
        <svg class="icon" viewBox="0 0 12 12"><path d="M6 0a6 6 0 1 0 0 12A6 6 0 0 0 6 0zm0 1c.7 0 1.5 1.6 1.7 4.5H4.3C4.5 2.6 5.3 1 6 1zM1 6.5h2.3c.1 1.6.4 3 .9 3.9A5 5 0 0 1 1 6.5zm0-1a5 5 0 0 1 3.2-3.9c-.5.9-.8 2.3-.9 3.9zm5 5.5c-.7 0-1.5-1.6-1.7-4.5h3.4C7.5 9.4 6.7 11 6 11zm1.8-.6c.5-.9.8-2.3.9-3.9H11a5 5 0 0 1-3.2 3.9zm.9-4.9c-.1-1.6-.4-3-.9-3.9A5 5 0 0 1 11 5.5z"/></svg>
        <div>www.steadywave.example</div>
      </li>
    </ul>
  </section>

  <section class="card card--back" aria-label="Card back">
    <div class="back-logo">
      <span class="wordmark">STEADYWAVE</span>
      <span class="logo-square"></span>
    </div>
    <div class="edge-strip--bottom"></div>
  </section>
</main>
</body>
</html>
```